Protein Powder Bag Design

We need a packaging design for a protein powder for our supplement company. The company is "Dawn Hollow" and the product is called "SUMMIT PROTEIN"

The bag design needs to include:

- Our Logo
- Grass-Fed Beef Isolate Powder
- Chocolate (as the flavor)
- 2lbs 900grams Dietary Supplement
- Matte finish

The back of the bag needs to include:

- Blurb about Dawn Hollow
i.e. Live Dawn Hollow for anything and part of that means dialing in your nutrition. We are about clean, real, whole foods, quality, transparency, health, performance, flexible lifestyle, convenience, paleo friendly, no gluten

- Supplement Facts (attached)
*Under Supplement Facts*
INGREDIENTS: Grass-Fed Beef Protein (CattlePRO TM), Cocoa Powder, Stevia Leaf Powder

- Barcode (attached)
- #eatrealfood
- info@dawnhollowfoods.example
- dawnhollowfoods.example
- Manufactured for Dawn Hollow, San Francisco, Ca 94107
- Collagen/Gellatin
- Complete source of protein
- Free from: dairy, gluten, whey, soy, antibiotics, hormones, fillers, artificial sweeteners, preservatives, and other nonsense.

- Suggested Use:
Mix with 8 to 10 oz of liquid or add to baked foods to feel amazing. Store in a dry, cool place.

- Ingredients Per Scoop:
4 oz grass-fed beef
Cocoa Powder
Stevia

- **These statements have not been evaluated by The Board of Nutrient Oversight. This product is not intended to diagnose, treat, cure or prevent disease.

• - Matte finish
• - Blue, white, color scheme
• - Check out the templates (do not copy)

```html
<!DOCTYPE html>
<html lang="en">
<head>
<meta charset="utf-8">
<title>Summit Protein – Chocolate Pouch Front</title>
<link rel="stylesheet" href="https://fonts.googleapis.com/css2?family=Barlow+Condensed:wght@500;600;700&display=swap">
<style>
  :root {
    --backdrop: #d6d6d6;
    --pouch-white: #f7f7f7;
    --pouch-edge: #e4e4e4;
    --brand-blue: #2b9ad6;
    --brand-blue-light: #55b8e6;
    --ink-dark: #252525;
    --ink-black: #0d0d0d;
    --cocoa-dark: #3b2119;
    --cocoa-mid: #7a4a33;
    --cocoa-light: #a9704f;
    --white: #ffffff;
  }
  * { box-sizing: border-box; margin: 0; padding: 0; }
  html, body { width: 1200px; height: 1200px; overflow: hidden; }
  body {
    background: var(--backdrop);
    font-family: "Barlow Condensed", "Arial Narrow", sans-serif;
    position: relative;
  }
  .pouch {
    position: absolute;
    left: 287px;
    top: 135px;
    width: 625px;
    height: 930px;
    background: linear-gradient(180deg, var(--pouch-white), #fdfdfd 60%, var(--pouch-white));
    border: 1px solid var(--pouch-edge);
    overflow: hidden;
  }
  .pouch-art { position: absolute; inset: 0; width: 625px; height: 930px; }
  .brand-name {
    position: absolute;
    left: 110px;
    top: 262px;
    width: 200px;
    text-align: center;
    color: var(--white);
    font-weight: 500;
    font-size: 24px;
    letter-spacing: 6px;
  }
  .product-title {
    position: absolute;
    left: 200px;
    top: 395px;
    width: 350px;
    text-align: center;
    font-weight: 600;
    line-height: 0.82;
  }
  .product-title .title-top { display: block; color: var(--ink-dark); font-size: 122px; }
  .product-title .title-bottom { display: block; color: var(--brand-blue); font-size: 100px; }
  .tagline {
    position: absolute;
    left: 196px;
    top: 590px;
    width: 344px;
    height: 36px;
    line-height: 36px;
    text-align: center;
    color: var(--white);
    font-weight: 600;
    font-size: 23px;
  }
  .weight-badge {
    position: absolute;
    left: 87px;
    top: 702px;
    width: 136px;
    height: 136px;
    border-radius: 50%;
    background: var(--ink-black);
    border: 3px solid var(--white);
    text-align: center;
    padding-top: 26px;
  }
  .weight-badge .weight-lbs { display: block; color: var(--brand-blue); font-weight: 600; font-size: 44px; line-height: 1; }
  .weight-badge .weight-grams { display: block; color: var(--white); font-weight: 500; font-size: 21px; margin-top: 6px; }
  .flavor-visual {
    position: absolute;
    left: 260px;
    top: 650px;
    width: 275px;
    height: 175px;
    border-radius: 50% 50% 45% 45%;
    background: radial-gradient(ellipse at 60% 45%, var(--cocoa-dark) 0%, var(--cocoa-mid) 45%, var(--cocoa-light) 65%, rgba(169,112,79,0) 72%);
  }
  .flavor-name {
    position: absolute;
    left: 260px;
    top: 848px;
    width: 275px;
    text-align: center;
    color: var(--cocoa-dark);
    font-weight: 600;
    font-size: 38px;
    letter-spacing: 2px;
  }
</style>
</head>
<body>
  <main class="pouch">
    <svg class="pouch-art" viewBox="0 0 625 930" aria-hidden="true">
      <rect class="seal-band" x="0" y="0" width="625" height="30" fill="#ececec"/>
      <line class="zip-line" x1="40" y1="100" x2="590" y2="100" stroke="#e2e2e2" stroke-width="3"/>
      <line class="zip-line" x1="40" y1="140" x2="590" y2="140" stroke="#e8e8e8" stroke-width="2"/>
      <path class="blue-wave" fill="var(--brand-blue)"
            d="M0,165 L380,165 C330,300 170,340 125,520 C95,650 110,830 215,930 L0,930 Z"/>
      <path class="blue-wave-edge" fill="none" stroke="var(--brand-blue-light)" stroke-width="3"
            d="M380,165 C330,300 170,340 125,520 C95,650 110,830 215,930"/>
      <path class="dark-side" fill="var(--ink-black)"
            d="M0,165 L30,165 C120,200 130,400 100,520 C70,640 45,760 55,930 L0,930 Z"/>
      <path class="dark-side-edge" fill="none" stroke="var(--white)" stroke-width="5"
            d="M30,165 C120,200 130,400 100,520 C70,640 45,760 55,930"/>
      <polygon class="tagline-ribbon" fill="var(--ink-dark)"
               points="196,590 540,590 528,608 540,626 196,626 208,608"/>
    </svg>

    <div class="brand-name">DAWN HOLLOW</div>

    <h1 class="product-title">
      <span class="title-top">SUMMIT</span>
      <span class="title-bottom">PROTEIN</span>
    </h1>

    <p class="tagline">GRASS-FED BEEF ISOLATE POWDER</p>

    <div class="weight-badge">
      <span class="weight-lbs">2 lbs</span>
      <span class="weight-grams">900 grams</span>
    </div>

    <div class="flavor-visual" role="img" aria-label="Photo of chocolate pieces resting on a pile of cocoa powder"></div>

    <p class="flavor-name">CHOCOLATE</p>
  </main>
</body>
</html>
```